My website design

It Will be a to-go website for all service requests from the comfort of your home. services ranging from renting an electrician to fix your home electrical issues, DJ for your party, mark-up artist for your wedding and so on. Here are a few websites for inspiration:

https://www.dwellnook.example/
https://www.chorefinch.example/
https://www.pinlatch.example/

Number of Pages Required

5+ page

Requirements
Must have
• User's registration form
pros resgistation form
filling out job request form
quotes sent sent back to job requester from various pros within the same zip code
quote accepted
ability to review pros once jobs are completed

```html
<!DOCTYPE html>
<html lang="en">
<head>
<meta charset="utf-8">
<title>Hestora — Home Maintenance Made Simple</title>
<link rel="stylesheet" href="https://fonts.googleapis.com/css2?family=Poppins:wght@300;400;500;600;700&display=swap">
<style>
:root{
  --green:#3bb44a;
  --slate:#5b6c78;
  --ink:#222a35;
  --text:#333c47;
  --muted:#8a9199;
  --mint:#f3f9f2;
  --paper:#f8f9f9;
  --navy:#1e2137;
  --navy-line:#2c3048;
  --white:#ffffff;
  --star:#f4a62a;
}
*{box-sizing:border-box;margin:0;padding:0}
html,body{width:1200px;height:2754px;overflow:hidden}
body{font-family:'Poppins',sans-serif;color:var(--text);background:var(--white);position:relative}
a{color:inherit;text-decoration:none}

/* header */
.site-header{position:absolute;top:0;left:0;width:1200px;height:83px;background:rgba(240,241,241,.96);z-index:3}
.brand{position:absolute;left:118px;top:22px;display:flex;align-items:center;gap:12px;font-weight:500;font-size:24px;letter-spacing:9px;color:var(--ink)}
.brand-mark{width:22px;height:22px;background:var(--green)}
.main-nav{position:absolute;left:507px;top:30px;display:flex;font-size:15px;font-weight:500;color:#3c4450}
.main-nav a{margin-right:40px}
.main-nav a.active{color:var(--green);text-decoration:underline}
.main-nav .gap{margin-right:55px}
.btn{display:inline-flex;align-items:center;justify-content:center;font-weight:500;font-size:15px}
.btn-green{background:var(--green);color:var(--white)}
.header-cta{position:absolute;left:917px;top:20px;width:166px;height:43px}
.nav-pointer{position:absolute;left:518px;top:83px;width:0;height:0;border-left:9px solid transparent;border-right:9px solid transparent;border-top:9px solid rgba(240,241,241,.96);z-index:3}

/* hero */
.hero{position:absolute;top:0;left:0;width:1200px;height:640px;overflow:hidden}
.hero-photo{position:absolute;inset:0;background:
 linear-gradient(rgba(20,22,28,.45),rgba(20,22,28,.45)),
 radial-gradient(ellipse at 30% 55%,#8a5a4e 0%,transparent 40%),
 radial-gradient(ellipse at 68% 30%,#3a4668 0%,transparent 45%),
 linear-gradient(100deg,#6d6661 0%,#857c76 30%,#5b5f70 55%,#8d8e92 85%,#b0b2b5 100%)}
.hero-copy{position:absolute;top:250px;left:0;width:1200px;text-align:center;color:var(--white)}
.hero-copy h1{font-size:45px;font-weight:600;line-height:54px}
.hero-copy p{font-size:19px;margin-top:10px}
.hero-search{position:absolute;left:357px;top:438px;width:487px;height:45px;border:2px solid var(--white);border-radius:23px;display:flex;overflow:hidden}
.hero-search .field{flex:1;display:flex;align-items:center;padding-left:27px;color:#d9dcdf;font-size:16px;background:rgba(255,255,255,.08)}
.hero-search .go{width:178px;background:var(--white);color:var(--ink);display:flex;align-items:center;justify-content:center;font-size:16px;font-weight:500}
.scroll-tab{position:absolute;left:569px;top:610px;width:62px;height:31px}

/* services */
.services{position:absolute;top:640px;left:0;width:1200px;height:362px;background:var(--mint)}
.services h2{position:absolute;left:118px;top:92px;font-size:27px;font-weight:400;color:var(--ink)}
.services h2 b,.testimonials h2 b{font-weight:600}
.services .lead{position:absolute;left:118px;top:135px;width:320px;font-size:15.5px;line-height:28px;color:var(--ink)}
.services .more{position:absolute;left:118px;top:206px;width:156px;height:45px}
.service-list{position:absolute;left:517px;top:96px;display:flex}
.service-item{width:175px;height:132px;margin-right:20px;display:flex;flex-direction:column;align-items:center;padding-top:16px;text-align:center;font-size:15.5px;line-height:21px;color:var(--slate)}
.service-item svg{width:46px;height:46px;margin-bottom:12px}
.service-item.active{background:var(--slate);color:var(--white);position:relative}
.service-item.active::after{content:"";position:absolute;bottom:-8px;left:80px;border-left:8px solid transparent;border-right:8px solid transparent;border-top:8px solid var(--slate)}

/* about */
.about{position:absolute;top:1002px;left:0;width:1200px;height:493px;background:var(--white)}
.rule{width:72px;height:3px;background:var(--green)}
.about .rule{position:absolute;left:188px;top:92px}
.about h2{position:absolute;left:189px;top:124px;font-size:27px;font-weight:400;line-height:38px;color:var(--ink)}
.about h2 b{font-weight:600;display:block}
.checks{position:absolute;left:188px;top:217px;list-style:none;font-size:16px;color:#4a525c}
.checks li{display:flex;align-items:center;height:39px}
.checks svg{width:16px;height:16px;margin-right:12px}
.about .learn{position:absolute;left:188px;top:354px;width:156px;height:48px;background:var(--slate);color:var(--white)}
.brand-frame{position:absolute;left:692px;top:89px;width:331px;height:316px;border:3px solid var(--green);display:flex;align-items:center;justify-content:center;font-size:40px;font-weight:600;letter-spacing:6px;color:var(--slate)}

/* testimonials */
.testimonials{position:absolute;top:1495px;left:0;width:1200px;height:592px;background:var(--paper)}
.testimonials .rule{position:absolute;left:116px;top:73px;width:65px}
.testimonials h2{position:absolute;left:116px;top:100px;font-size:27px;font-weight:400;color:var(--ink)}
.cards{position:absolute;left:117px;top:181px;display:flex;gap:25px}
.card{width:306px;height:292px;border:2px solid #e3e6e8;background:var(--paper);padding:0 31px}
.avatar{width:68px;height:68px;border-radius:50%;background:linear-gradient(#e9d9c9,#c9a88a);margin:24px auto 0;border:2px solid #fff;box-shadow:0 0 0 1px #e0e0e0}
.card-head{display:flex;align-items:center;margin-top:19px;font-size:15px;font-weight:500;color:var(--ink)}
.stars{color:var(--star);font-size:14px;letter-spacing:1px;margin-left:12px}
.card p{font-size:12.5px;line-height:23px;color:#4a525c;margin-top:7px}
.card .date{font-size:14px;color:var(--muted);margin-top:9px}
.card .tag{font-size:14px;color:var(--green);margin-top:5px}
.dots{position:absolute;left:564px;top:507px;display:flex;align-items:center;gap:9px}
.dots span{width:10px;height:10px;border-radius:50%;background:#a9dcaf}
.dots span.on{width:14px;height:14px;background:var(--green)}

/* cta */
.cta{position:absolute;top:2087px;left:0;width:1200px;height:233px;background:var(--green);overflow:hidden;color:var(--white)}
.cta h2{position:absolute;left:123px;top:61px;font-size:32px;font-weight:600}
.cta p{position:absolute;left:123px;top:114px;font-size:30px;font-weight:300}
.cta .book{position:absolute;left:885px;top:96px;width:199px;height:47px;background:var(--white);color:var(--green);border-radius:24px;font-size:16px}

/* footer */
.site-footer{position:absolute;top:2320px;left:0;width:1200px;height:434px;background:var(--navy);color:#c9ccd8}
.footer-brand{position:absolute;left:118px;top:96px;display:flex;align-items:center;gap:12px;font-size:27px;font-weight:500;letter-spacing:10px;color:var(--white)}
.footer-brand .brand-mark{width:24px;height:24px}
.phone{position:absolute;left:117px;top:183px;font-size:19px;color:var(--white);letter-spacing:.5px}
.footer-note{position:absolute;left:116px;top:232px;font-size:13px;line-height:24px;color:#b7bbca}
.footer-col h3{font-size:15px;font-weight:600;color:var(--white);margin-bottom:16px}
.links{position:absolute;left:500px;top:87px}
.links ul{list-style:none;font-size:14px;line-height:26.5px;color:#b7bbca}
.newsletter{position:absolute;left:732px;top:87px;width:352px}
.newsletter h3{font-size:14px;margin-bottom:14px}
.newsletter p{font-size:12px;color:#b7bbca}
.subscribe{display:flex;margin-top:16px;height:38px;width:349px;border-radius:19px;overflow:hidden;margin-left:2px}
.subscribe .field{flex:1;background:#eef3f8;color:#7c8593;font-size:14px;display:flex;align-items:center;padding-left:25px}
.subscribe .send{width:119px;background:var(--green);color:var(--white);font-size:14px;font-weight:600;display:flex;align-items:center;justify-content:center}
.follow{margin-top:22px;font-size:13px;font-weight:600;color:var(--white)}
.socials{display:flex;gap:10px;margin-top:12px;padding:6px 8px;background:#252941;width:134px}
.socials span{width:16px;height:16px;border-radius:50%;background:#8f94a8}
.copyright{position:absolute;left:0;top:337px;width:1200px;height:97px;border-top:1px solid var(--navy-line);text-align:center;padding-top:40px;font-size:14px;color:#b7bbca}
</style>
</head>
<body>

<section class="hero">
  <div class="hero-photo" role="img" aria-label="Electrician testing wires with a multimeter while a homeowner waits in the background"></div>
  <div class="hero-copy">
    <h1>Home Maintenance<br>Made simple</h1>
    <p>One Call Can Solve All Your House Problems</p>
  </div>
  <div class="hero-search">
    <div class="field">What Services do you need</div>
    <a class="go" href="#">Get Help Today</a>
  </div>
  <svg class="scroll-tab" viewBox="0 0 62 31"><path d="M0 31 L31 0 L62 31 Z" fill="#f3f9f2"/><path d="M26 20 L31 25 L36 20" stroke="#3bb44a" stroke-width="1.6" fill="none"/></svg>
</section>

<header class="site-header">
  <a class="brand" href="#"><span class="brand-mark"></span>HESTORA</a>
  <nav class="main-nav">
    <a class="active gap" href="#">Home</a>
    <a href="#">Services</a>
    <a class="gap" href="#">Contact</a>
    <a href="#">Login</a>
  </nav>
  <a class="btn btn-green header-cta" href="#">Book A Services</a>
</header>
<div class="nav-pointer"></div>

<section class="services">
  <h2>Our <b>Services</b></h2>
  <p class="lead">Lorem Ipsum is simply dummy text of the printing and typesetting industry.</p>
  <a class="btn btn-green more" href="#">More Services</a>
  <div class="service-list">
    <div class="service-item">
      <svg viewBox="0 0 46 46" fill="none" stroke="#3bb44a" stroke-width="2"><path d="M8 6v8M14 6v8M5 14h12v6a6 6 0 0 1-12 0z"/><circle cx="27" cy="24" r="9"/><path d="M33 31l6 8M36 29l6 6"/></svg>
      Electrician<br>Services
    </div>
    <div class="service-item active">
      <svg viewBox="0 0 46 46" fill="none" stroke="#fff" stroke-width="1.6"><rect x="3" y="4" width="40" height="38"/><path d="M10 12v24M18 12v24M26 12v24M8 20h4M16 28h4M24 16h4"/><circle cx="35" cy="34" r="5"/><path d="M31 12h8v8h-8z"/></svg>
      DJ For Your<br>Party Services
    </div>
    <div class="service-item">
      <svg viewBox="0 0 46 46" fill="none" stroke="#3bb44a" stroke-width="2"><circle cx="17" cy="28" r="11"/><circle cx="29" cy="28" r="11"/><path d="M13 12l4-5 4 5-4 4z"/></svg>
      Mark-Up Artist<br>For Wedding
    </div>
  </div>
</section>

<section class="about">
  <div class="rule"></div>
  <h2>A simple way To <b>Take Care of Everything</b></h2>
  <ul class="checks">
    <li><svg viewBox="0 0 16 16" fill="none" stroke="#3bb44a" stroke-width="1.4"><circle cx="8" cy="8" r="6.5"/><path d="M5 8.2l2 2 4-4.2"/></svg>Trusted technicians in your neighborhood</li>
    <li><svg viewBox="0 0 16 16" fill="none" stroke="#3bb44a" stroke-width="1.4"><circle cx="8" cy="8" r="6.5"/><path d="M5 8.2l2 2 4-4.2"/></svg>Guaranteed parts and service + 24/7 support</li>
    <li><svg viewBox="0 0 16 16" fill="none" stroke="#3bb44a" stroke-width="1.4"><circle cx="8" cy="8" r="6.5"/><path d="M5 8.2l2 2 4-4.2"/></svg>Hundreds of repair and install options</li>
  </ul>
  <a class="btn learn" href="#">Learn More</a>
  <div class="brand-frame">HESTORA</div>
</section>

<section class="testimonials">
  <div class="rule"></div>
  <h2>Don't just take <b>our word for it</b></h2>
  <div class="cards">
    <article class="card">
      <div class="avatar" role="img" aria-label="Client portrait"></div>
      <div class="card-head">Client Name <span class="stars">★★★★★</span></div>
      <p>Lorem Ipsum is simply dummy text of the printing and typesetting industry. Lorem Ipsum has been the industry's</p>
      <div class="date">October 11, 2019</div>
      <div class="tag">Electrician Services</div>
    </article>
    <article class="card">
      <div class="avatar" role="img" aria-label="Client portrait"></div>
      <div class="card-head">Client Name <span class="stars">★★★★★</span></div>
      <p>Lorem Ipsum is simply dummy text of the printing and typesetting industry. Lorem Ipsum has been the industry's</p>
      <div class="date">October 11, 2019</div>
      <div class="tag">Electrician Services</div>
    </article>
    <article class="card">
      <div class="avatar" role="img" aria-label="Client portrait"></div>
      <div class="card-head">Client Name <span class="stars">★★★★★</span></div>
      <p>Lorem Ipsum is simply dummy text of the printing and typesetting industry. Lorem Ipsum has been the industry's</p>
      <div class="date">October 11, 2019</div>
      <div class="tag">Electrician Services</div>
    </article>
  </div>
  <div class="dots"><span></span><span class="on"></span><span></span><span></span></div>
</section>

<section class="cta">
  <h2>Ready to getstarted?</h2>
  <p>A simple way to take care of everything</p>
  <a class="btn book" href="#">Book A Services</a>
</section>

<footer class="site-footer">
  <div class="footer-brand"><span class="brand-mark"></span>HESTORA</div>
  <div class="phone">+100 &nbsp;(555-0199)</div>
  <p class="footer-note">It's time to Step-up Your Social Media Game<br>and leave your competition behind</p>
  <div class="footer-col links">
    <h3>Quick Links</h3>
    <ul><li>Home</li><li>About Us</li><li>Services</li><li>Book A Services</li><li>Site Map</li><li>Contact Us</li></ul>
  </div>
  <div class="footer-col newsletter">
    <h3>WRITE TO US</h3>
    <p>Provide your email below to subscribe to our newsletter</p>
    <div class="subscribe"><div class="field">Email address</div><a class="send" href="#">Subscribe</a></div>
    <div class="follow">FOLLOW US</div>
    <div class="socials"><span></span><span></span><span></span><span></span><span></span></div>
  </div>
  <div class="copyright">Copyright 2020 hestora.example</div>
</footer>

</body>
</html>
```